Website design for staffing/workforce solutions company - Halvard Staffing Solutions

Create a launch-ready website
Halvard Staffing Solutions also known as HSS. This is a company that specializes in Staffing/Work force solutions for Healthcare/IT/Logistics/Maintenance/Construction/Manufacturing/Industrial/General Labor. HSS works with government agencies/contracts also. Use the attached logo in the build of the website. Website should be clean, modern, engaging, innovative. Website needs to speak to the professional services industry.
Halvard Staffing Solutions or HSS is a certified VOSB, SDVOSB, DBE and Minority-Owned Business.
The website needs to be compliant for government contracting.

Website needs to include the following--
Modern UI/UX Enhancements: A hero section with a strong call-to-action.
Government Contracting Compliance: Certification display and a Capability Statement download.
Advanced Careers Section: A dedicated job application portal.
Social Media & Lead Generation: Links to Profilary, Quillo, and Mingleo.
Security & Performance: Optimized for SEO, fast loading, and mobile responsiveness.
1. Modern Design Upgrades
๐Ÿ”น Upgrade UI/UX for a Professional, Trustworthy Look
โœ… Full-width hero banner with a high-quality background image representing business, technology, and workforce solutions.
โœ… Animated elements (subtle transitions for smooth browsing experience).
โœ… Bold CTA buttons for easy navigation to key actions (e.g., โ€œGet Startedโ€ or โ€œRequest a Consultationโ€).
โœ… Dark-themed header with contrasting colors (professional & government-trustworthy).
โœ… New Homepage Hero Section Example:
"Your Trusted Partner in Workforce, IT, Maintenance & Logistics Solutions"
Button: "Discover Our Services"

2. Enhanced Government Contracting Section (Key for Compliance)
๐Ÿ“Œ Essential for securing contracts & building credibility
โœ… Capability Statement (Downloadable PDF)

Showcase key past contracts, company qualifications, and services in a downloadable format for government buyers.
โœ… Certifications Display (VOSB, SDVOSB, DBE, Minority-Owned Business)

Visual badge display to emphasize legitimacy for government contracts.
โœ… Procurement Readiness Details

NAICS Codes, DUNS Number, CAGE Code, and relevant VPR.example registration details.
โœ… Past Performance Showcase (Case Studies Section)

Highlight successful projects and government contracts.
โœ… Compliance & Security

Add SOC 2, HIPAA (for healthcare staffing), and ITAR compliance if applicable.
3. Advanced Job Search & Candidate Portal (For Staffing Services)
๐Ÿ“Œ To attract top talent for staffing contracts

โœ… Advanced Job Search Feature

Filters: Industry, location, job type (contract/full-time), salary range, and clearance level (for government jobs).
โœ… Candidate Login Portal

Applicants can upload resumes, track applications, and receive job alerts.
โœ… Employer Portal (For Businesses Hiring Through HSS)

A dedicated section for companies to submit staffing requests and view candidate matches.
4. Service-Specific Landing Pages (SEO & Engagement)
๐Ÿ“Œ Helps different industries find relevant services faster

๐Ÿ”น Dedicated Pages for Each Service:
โœ… Staffing & Workforce Solutions

Specialized sections for Healthcare, IT, Construction, Industrial, and General Labor staffing.
โœ… IT Services

List services like Cybersecurity, Cloud Solutions, and IT Consulting.
Showcase tech stack & certifications.
โœ… Logistics & Maintenance

Detail fleet management, supply chain services, and industrial maintenance.
โœ… Government Contracting Solutions

A streamlined page for government agencies.
5. Security & Compliance Upgrades (For Government Work)
๐Ÿ“Œ To ensure compliance & credibility in government contracting

โœ… SSL Certification (100% Required for Security)

Secure client and job applicant data.
โœ… ADA Compliance (Accessibility)

Ensure the website follows WCAG 2.1 accessibility standards for government clients.
โœ… GDPR & Data Protection Features

A privacy policy and terms of service to comply with data regulations.
6. Performance & Mobile Optimization
๐Ÿ“Œ To ensure fast loading & responsiveness

โœ… Mobile-Responsive Design

Optimized for mobile-friendly navigation since many users browse from phones.
โœ… Fast-Loading Pages

Optimize images & implement lazy loading for better site speed.
โœ… SEO-Optimized Pages

Improve search ranking on Searvo with:
Keyword-optimized content (e.g., โ€œGovernment Contracting Staffing Servicesโ€)
Schema markup for job listings
Blog/articles about staffing trends
7. Social Media & Lead Generation
๐Ÿ“Œ For brand credibility & client engagement

โœ… Profilary, Quillo, Mingleo Integration

Display recent updates from Profilary (primary for B2B & government).
โœ… Lead Capture Forms

Forms for business inquiries, talent applications, and government RFPs.
โœ… Client & Candidate Testimonials
Showcase client success stories & employee experiences

Good websites to pull examples for inspiration/direction--
https://www.pelmora.example/
https://www.tovrinex.example/
https://brambleworks.example/homepage/
https://www.quantelvetting.example/capability-statement

Staffing/Professional Services

Coded - Design and coding required

5+ page

• Website needs to include the following-- Modern UI/UX Enhancements: A hero section with a strong call-to-action. Government Contracting Compliance: Certification display and a Capability Statement download. Advanced Careers Section: A dedicated job application portal. Social Media & Lead Generation: Links to Profilary, Quillo, and Mingleo. Security & Performance: Optimized for SEO, fast loading, and mobile responsiveness. 1. Modern Design Upgrades ๐Ÿ”น Upgrade UI/UX for a Professional, Trustworthy Look โœ… Full-width hero banner with a high-quality background image representing business, technology, and workforce solutions. โœ… Animated elements (subtle transitions for smooth browsing experience). โœ… Bold CTA buttons for easy navigation to key actions (e.g., โ€œGet Startedโ€ or โ€œRequest a Consultationโ€). โœ… Dark-themed header with contrasting colors (professional & government-trustworthy). โœ… New Homepage Hero Section Example: "Your Trusted Partner in Workforce, IT, & Logistics Solutions" Button: "Discover Our Services" 2. Enhanced Government Contracting Section (Key for Compliance) ๐Ÿ“Œ Essential for securing contracts & building credibility โœ… Capability Statement (Downloadable PDF) Showcase key past contracts, company qualifications, and services in a downloadable format for government buyers. โœ… Certifications Display (VOSB, SDVOSB, DBE, Minority-Owned Business) Visual badge display to emphasize legitimacy for government contracts. โœ… Procurement Readiness Details NAICS Codes, DUNS Number, CAGE Code, and relevant VPR.example registration details. โœ… Past Performance Showcase (Case Studies Section) Highlight successful projects and government contracts. โœ… Compliance & Security Add SOC 2, HIPAA (for healthcare staffing), and ITAR compliance if applicable. 3. Advanced Job Search & Candidate Portal (For Staffing Services) ๐Ÿ“Œ To attract top talent for staffing contracts โœ… Advanced Job Search Feature Filters: Industry, location, job type (contract/full-time), salary range, and clearance level (for government jobs). โœ… Candidate Login Portal Applicants can upload resumes, track applications, and receive job alerts. โœ… Employer Portal (For Businesses Hiring Through HSS) A dedicated section for companies to submit staffing requests and view candidate matches. 4. Service-Specific Landing Pages (SEO & Engagement) ๐Ÿ“Œ Helps different industries find relevant services faster ๐Ÿ”น Dedicated Pages for Each Service: โœ… Staffing & Workforce Solutions Specialized sections for Healthcare, IT, Construction, Industrial, and General Labor staffing. โœ… IT Services List services like Cybersecurity, Cloud Solutions, and IT Consulting. Showcase tech stack & certifications. โœ… Logistics & Maintenance Detail fleet management, supply chain services, and industrial maintenance. โœ… Government Contracting Solutions A streamlined page for government agencies. 5. Security & Compliance Upgrades (For Government Work) ๐Ÿ“Œ To ensure compliance & credibility in government contracting โœ… SSL Certification (100% Required for Security) Secure client and job applicant data. โœ… ADA Compliance (Accessibility) Ensure the website follows WCAG 2.1 accessibility standards for government clients. โœ… GDPR & Data Protection Features A privacy policy and terms of service to comply with data regulations. 6. Performance & Mobile Optimization ๐Ÿ“Œ To ensure fast loading & responsiveness โœ… Mobile-Responsive Design Optimized for mobile-friendly navigation since many users browse from phones. โœ… Fast-Loading Pages Optimize images & implement lazy loading for better site speed. โœ… SEO-Optimized Pages Improve search ranking on Searvo with: Keyword-optimized content (e.g., โ€œGovernment Contracting Staffing Servicesโ€) Schema markup for job listings Blog/articles about staffing trends 7. Social Media & Lead Generation ๐Ÿ“Œ For brand credibility & client engagement โœ… Profilary, Quillo, Mingleo Integration Display recent updates from Profilary (primary for B2B & government). โœ… Lead Capture Forms Forms for business inquiries, talent applications, and government RFPs. โœ… Client & Candidate Testimonials Showcase client success stories & employee experiences Good websites to pull examples for inspiration/direction-- https://www.pelmora.example/ https://www.tovrinex.example/ https://brambleworks.example/homepage/

```html
<!DOCTYPE html>
<html lang="en">
<head>
<meta charset="utf-8">
<title>Halvard Staffing Solutions — Workforce, IT &amp; Logistics</title>
<link href="https://fonts.googleapis.com/css2?family=Montserrat:ital,wght@0,400;0,500;0,600;0,700;1,400&display=swap" rel="stylesheet">
<style>
:root{
  --red:#e1141b;
  --red-dark:#a50d12;
  --ink:#1b1b1b;
  --text:#3a3a3a;
  --muted:#6b6b6b;
  --line:#d8d8d8;
  --light:#f1f1f1;
  --dark:#151515;
  --white:#ffffff;
}
*{margin:0;padding:0;box-sizing:border-box}
html,body{width:1200px;height:4612px;overflow:hidden}
body{font-family:"Montserrat",Arial,sans-serif;color:var(--text);background:var(--white);position:relative}
.abs{position:absolute}
.red{color:var(--red)}
.btn{position:absolute;display:flex;align-items:center;justify-content:center;gap:8px;background:var(--red);color:var(--white);font-weight:700;font-size:13px;letter-spacing:.3px;text-transform:uppercase;text-decoration:none}
.photo{position:absolute}

/* Header + hero */
.hero{position:absolute;left:0;top:0;width:1200px;height:722px;background:linear-gradient(90deg,#141414 0%,#1d1d1d 45%,#2a2420 100%);overflow:hidden}
.hero-photo{left:537px;top:0;width:663px;height:722px;background:radial-gradient(ellipse at 55% 50%,#6a5a48 0%,#3a332c 45%,#1a1a1a 85%)}
.logo{position:absolute;display:flex;flex-direction:column;align-items:flex-start}
.logo-name{font-weight:700;font-size:30px;letter-spacing:1px;color:var(--white);line-height:1}
.logo-sub{font-weight:600;font-size:7px;letter-spacing:1.1px;color:var(--white);margin-top:6px}
.nav{position:absolute;top:41px;left:376px}
.nav a{position:absolute;white-space:nowrap;color:var(--white);font-size:12px;font-weight:600;text-decoration:none}
.hero-frame{left:116px;top:254px;width:502px;height:256px;border:1px solid var(--red)}
.hero-title{left:149px;top:232px;font-size:32px;font-weight:600;line-height:44px;color:var(--white);text-transform:uppercase;white-space:nowrap}
.hero-title .red{background:#1a1a1a;padding-right:6px}
.hero-text{left:152px;top:374px;width:440px;font-size:13px;line-height:23px;color:#e6e6e6}

/* Government contracting */
.gov-title{left:138px;top:806px;font-size:35px;font-weight:700;line-height:44px;text-transform:uppercase;color:var(--ink)}
.gov-title span{display:block}
.gov-bar{left:120px;top:808px;width:3px;height:80px;background:var(--red)}
.gov-intro{left:508px;top:818px;width:540px;font-size:16px;line-height:27px;color:var(--text)}
.tab{position:absolute;top:935px;width:186px;height:73px;border:2px solid var(--line);display:flex;align-items:center;justify-content:center;text-align:center;font-size:14px;font-weight:600;line-height:20px;color:var(--ink)}
.tab.active{background:var(--dark);border-color:var(--dark);color:var(--white)}
.tab.active::after{content:"";position:absolute;bottom:-12px;left:50%;margin-left:-11px;border-left:11px solid transparent;border-right:11px solid transparent;border-top:12px solid var(--dark)}
.cap-card{position:absolute;top:1064px;width:308px;height:365px;border:2px solid #e3e3e3;background:var(--white)}
.cap-icon{position:absolute;left:32px;top:20px;width:72px;height:72px;border-radius:50%;background:#efefef;display:flex;align-items:center;justify-content:center}
.cap-head{position:absolute;left:40px;top:104px;font-size:19px;font-weight:700;line-height:22px;text-transform:uppercase;color:var(--ink)}
.cap-head::before{content:"";position:absolute;left:-40px;top:0;width:3px;height:44px;background:var(--ink)}
.cap-body{position:absolute;left:40px;top:165px;width:245px;font-size:12.5px;line-height:23px;color:var(--text)}
.cap-list{list-style:none;position:absolute;left:40px;top:154px;width:260px}
.cap-list li{font-size:12.5px;line-height:31px;color:var(--ink);padding-left:14px;position:relative;white-space:nowrap}
.cap-list li::before{content:"";position:absolute;left:0;top:13px;width:5px;height:5px;border-radius:50%;background:var(--red)}
.cap-btn{left:34px;top:281px;width:194px;height:45px;justify-content:flex-start;padding-left:30px;font-size:12px}
.cap-btn .dl{position:absolute;right:0;top:0;width:44px;height:45px;border-left:1px solid rgba(255,255,255,.5);display:flex;align-items:center;justify-content:center}

/* About */
.about{position:absolute;left:0;top:1497px;width:1200px;height:595px;background:linear-gradient(90deg,#f4f4f4,#ececec)}
.about-red{left:106px;top:66px;width:188px;height:120px;background:var(--red)}
.about-main{left:111px;top:68px;width:444px;height:387px;background:var(--white);padding:10px}
.about-main .photo,.about-sub .photo{position:relative;width:100%;height:100%}
.about-sub{left:326px;top:286px;width:290px;height:225px;background:var(--white);padding:4px}
.eyebrow{font-size:14px;font-weight:600;letter-spacing:2px;text-transform:uppercase;color:var(--ink)}
.section-title{font-size:35px;font-weight:700;text-transform:uppercase;color:var(--ink);line-height:42px}
.about-text{left:655px;top:202px;width:450px;font-size:16.5px;line-height:27px;color:var(--ink)}
.about-text p+p{margin-top:27px}
.about-line{left:978px;top:123px;width:222px;height:1px;background:#bcbcbc}
.about-dot{left:973px;top:119px;width:9px;height:9px;border-radius:50%;background:var(--red)}
.stem{left:601px;top:2060px;width:1px;height:60px;background:#9a9a9a}
.stem-dot{left:598px;top:2117px;width:7px;height:7px;border-radius:50%;background:var(--red)}

/* Careers */
.center{left:0;width:1200px;text-align:center}
.careers-panel{left:125px;top:2301px;width:967px;height:301px;background:#e6e6e6}
.job{position:absolute;top:2316px;width:299px;height:272px;background:var(--white);border:2px solid #cfcfcf}
.job-tag{position:absolute;left:38px;top:46px;background:#fde5e5;color:var(--red);font-size:9.5px;font-weight:600;padding:3px 6px;text-transform:uppercase;letter-spacing:.3px}
.job-title{position:absolute;left:38px;top:74px;font-size:19px;font-weight:600;color:var(--ink)}
.job-text{position:absolute;left:38px;top:108px;width:235px;font-size:14px;line-height:22px;color:var(--ink)}
.job-btn{left:38px;top:191px;width:158px;height:38px;font-size:12.5px}
.dot-nav{position:absolute;top:2639px;width:36px;height:3px;background:#bdbdbd}
.dot-nav.on{background:var(--dark)}

/* Testimonials */
.testi{position:absolute;left:0;top:2717px;width:1200px;height:550px;background:linear-gradient(180deg,#1b1b1b 0%,#252525 50%,#2e2e2e 100%)}
.testi .eyebrow{color:var(--white)}
.testi .section-title{color:var(--white)}
.quote{position:absolute;top:179px;width:457px;height:274px;border:2px solid var(--red)}
.quote-mark{position:absolute;left:50px;top:-40px;font-size:110px;font-weight:700;color:var(--white);line-height:1;font-family:Georgia,serif;background:#232323;padding:0 8px;height:60px;overflow:hidden}
.quote-text{position:absolute;left:42px;top:52px;width:370px;font-size:14.5px;line-height:25.5px;font-style:italic;color:#9d9d9d}
.quote-name{position:absolute;left:42px;top:186px;font-size:17px;color:var(--white)}
.quote-stars{position:absolute;left:42px;top:212px;font-size:17px;letter-spacing:2px;color:var(--white)}

/* Blogs */
.blog-big{left:147px;top:3447px;width:467px;height:366px;background:linear-gradient(160deg,#7a6c5e 0%,#4a4038 55%,#1f1b18 100%)}
.blog-big .date{left:33px;top:237px}
.date{position:absolute;background:var(--red);color:var(--white);font-size:10px;font-weight:600;padding:4px 10px}
.blog-big h3{position:absolute;left:33px;top:268px;font-size:19px;font-weight:700;color:var(--white)}
.blog-big p{position:absolute;left:33px;top:302px;width:390px;font-size:12.5px;line-height:20px;color:#e0e0e0}
.blog-small{position:absolute;left:638px;width:438px;height:172px;background:var(--white);border:1px solid #cfcfcf}
.blog-small .photo{left:0;top:0;width:209px;height:100%}
.blog-small .date{left:237px;top:40px}
.blog-small h3{position:absolute;left:237px;top:68px;font-size:17.5px;font-weight:600;color:var(--ink)}
.blog-small p{position:absolute;left:237px;top:98px;width:180px;font-size:11.5px;line-height:19px;color:var(--muted)}

/* CTA + footer */
.footer{position:absolute;left:0;top:4107px;width:1200px;height:505px;background:#161616;overflow:hidden}
.footer-mark{position:absolute;left:0;width:1200px;top:340px;text-align:center;font-size:200px;font-weight:700;letter-spacing:6px;color:#1f1f1f;line-height:1}
.cta{left:136px;top:3942px;width:953px;height:274px;background:linear-gradient(110deg,#c30d13 0%,#d4141a 55%,#a10c10 100%);border-radius:4px;overflow:hidden}
.cta-glow{position:absolute;left:560px;top:0;width:393px;height:274px;background:linear-gradient(135deg,rgba(255,255,255,0) 30%,rgba(255,255,255,.12) 55%,rgba(255,255,255,0) 75%)}
.cta .eyebrow{position:absolute;left:83px;top:77px;color:var(--white);font-size:13px}
.cta h2{position:absolute;left:83px;top:101px;font-size:30px;font-weight:700;color:var(--white);text-transform:uppercase}
.cta p{position:absolute;left:83px;top:147px;width:450px;font-size:12.5px;line-height:22px;color:#f5dcdc}
.cta-btn{left:718px;top:109px;width:181px;height:47px;background:transparent;border:1.5px solid var(--white);font-weight:600;font-size:14px}
.foot-col{position:absolute;top:183px}
.foot-col h4{font-size:17px;font-weight:600;color:var(--white);text-transform:uppercase;position:relative}
.foot-col h4::before{content:"";position:absolute;left:-16px;top:2px;width:3px;height:19px;background:var(--red)}
.foot-col ul{list-style:none;margin-top:10px}
.foot-col li{font-size:12.5px;line-height:29px;color:#c2c2c2}
.social{position:absolute;top:275px;display:flex;align-items:center;gap:6px;font-size:13px;font-weight:600;color:var(--white)}
.social i{display:inline-block;width:10px;height:10px;border-radius:50%;background:var(--red)}
.copy{position:absolute;left:0;top:452px;width:1200px;text-align:center;font-size:12px;color:#c2c2c2}
</style>
</head>
<body>

<header class="hero">
  <div class="photo hero-photo" role="img" aria-label="Photo of colleagues reviewing work together at a laptop in a dim office"></div>
  <div class="logo" style="left:116px;top:24px">
    <span class="logo-name">HALVARD</span>
    <span class="logo-sub">PARTNERING FOR YOUR BUSINESS SUCCESS</span>
  </div>
  <nav class="nav">
    <a style="left:0">HOME</a>
    <a style="left:75px">GOVERTMENT CONTRACTING</a>
    <a style="left:306px">JOBS</a>
    <a style="left:378px">SERVICES</a>
    <a style="left:480px">CONTACT US</a>
  </nav>
  <a class="btn" style="left:980px;top:29px;width:147px;height:36px;font-weight:600;font-size:12px">GET STARTED ›</a>
  <div class="abs hero-frame"></div>
  <h1 class="abs hero-title"><span class="red">YOUR TRUSTED PARTNER</span><br>IN WORKFORCE, IT, &amp;<br>LOGISTICS SOLUTIONS</h1>
  <p class="abs hero-text">Lorem ipsum dolor sit amet consectetur adipiscing elit, sed do eiusmod tempor incididunt ut labore et dolore magna.</p>
  <a class="btn" style="left:152px;top:439px;width:251px;height:46px">DISCOVER OUR SERVICES ›</a>
</header>

<section class="gov">
  <div class="abs gov-bar"></div>
  <h2 class="abs gov-title"><span class="red">GOVERNMENT</span><span>CONTRACTING</span></h2>
  <p class="abs gov-intro">Lorem ipsum dolor sit amet, consectetur adipiscing elit, sed do eiusmod tempor incididunt ut labore et dolore</p>

  <div class="tab active" style="left:122px">Capability<br>Statement</div>
  <div class="tab" style="left:319px">Certifications<br>Display</div>
  <div class="tab" style="left:516px">Procurement<br>Readiness Details</div>
  <div class="tab" style="left:713px">Past Performance<br>Showcas</div>
  <div class="tab" style="left:908px">Compliance &amp;<br>Security</div>

  <article class="cap-card" style="left:116px">
    <div class="cap-icon"><svg width="38" height="38" viewBox="0 0 38 38" fill="none" stroke="#222" stroke-width="1.6"><rect x="8" y="6" width="18" height="26" rx="1"/><line x1="12" y1="13" x2="22" y2="13"/><line x1="12" y1="18" x2="22" y2="18"/><line x1="12" y1="23" x2="19" y2="23"/><circle cx="28" cy="11" r="5" stroke="#e1141b"/></svg></div>
    <h3 class="cap-head"><span class="red">KEY PAST</span><br>CONTRACTS</h3>
    <p class="cap-body">Lorem ipsum dolor sit amet, consectetur adipiscing elit, sed do eiusmod tempor incididunt ut labore et dolore magna</p>
    <a class="btn cap-btn">DOWNLAOP PDF<span class="dl"><svg width="18" height="18" viewBox="0 0 18 18" fill="none" stroke="#fff" stroke-width="1.6"><path d="M9 2v10M5 8l4 4 4-4M2 13v3h14v-3"/></svg></span></a>
  </article>
  <article class="cap-card" style="left:446px">
    <div class="cap-icon"><svg width="38" height="38" viewBox="0 0 38 38" fill="none" stroke="#222" stroke-width="1.6"><rect x="9" y="5" width="20" height="28" rx="1"/><path d="M13 12l2 2 3-3M13 19l2 2 3-3M13 26l2 2 3-3" stroke="#e1141b"/><line x1="21" y1="13" x2="26" y2="13"/><line x1="21" y1="20" x2="26" y2="20"/><line x1="21" y1="27" x2="26" y2="27"/></svg></div>
    <h3 class="cap-head"><span class="red">COMPANY</span><br>QUALIFICATIONS</h3>
    <ul class="cap-list">
      <li>Lorem ipsum dolor sit amet</li>
      <li>Consectetur adipiscing</li>
      <li>Elit sed do eiusmod</li>
    </ul>
    <a class="btn cap-btn">DOWNLAOP PDF<span class="dl"><svg width="18" height="18" viewBox="0 0 18 18" fill="none" stroke="#fff" stroke-width="1.6"><path d="M9 2v10M5 8l4 4 4-4M2 13v3h14v-3"/></svg></span></a>
  </article>
  <article class="cap-card" style="left:776px">
    <div class="cap-icon"><svg width="38" height="38" viewBox="0 0 38 38" fill="none" stroke="#222" stroke-width="1.6"><circle cx="19" cy="12" r="5" stroke="#e1141b"/><circle cx="10" cy="20" r="3.5"/><circle cx="28" cy="20" r="3.5"/><path d="M11 32c0-5 4-8 8-8s8 3 8 8M3 31c0-4 3-6 7-6M35 31c0-4-3-6-7-6"/></svg></div>
    <h3 class="cap-head" style="line-height:44px"><span class="red">SERVICES</span> PROVIDE</h3>
    <ul class="cap-list" style="left:42px;top:138px">
      <li>Staffing &amp; Workforce Solutions</li>
      <li>IT Services</li>
      <li>Logistics &amp; Maintenance</li>
      <li>Government Contracting Solutions</li>
    </ul>
    <a class="btn cap-btn" style="top:281px">DOWNLAOP PDF<span class="dl"><svg width="18" height="18" viewBox="0 0 18 18" fill="none" stroke="#fff" stroke-width="1.6"><path d="M9 2v10M5 8l4 4 4-4M2 13v3h14v-3"/></svg></span></a>
  </article>
</section>

<section class="about">
  <div class="abs about-red"></div>
  <div class="abs about-main"><div class="photo" role="img" aria-label="Photo of a team discussing papers in a bright office" style="background:linear-gradient(135deg,#8a6f52 0%,#c8a878 40%,#6b5a48 100%)"></div></div>
  <div class="abs about-sub"><div class="photo" role="img" aria-label="Photo of colleagues meeting around a table with laptops" style="background:linear-gradient(135deg,#2b2b2b 0%,#5a4d42 55%,#8b7a66 100%)"></div></div>
  <div class="abs about-line"></div>
  <div class="abs about-dot"></div>
  <div class="abs" style="left:655px;top:118px">
    <p class="eyebrow" style="font-size:13px">WHO WE ARE</p>
    <h2 class="section-title" style="margin-top:14px"><span class="red">ABOUT</span> HALVARD</h2>
  </div>
  <div class="abs about-text">
    <p>Lorem ipsum dolor sit amet, consectetur adipiscing elit, sed do eiusmod tempor incididunt ut</p>
    <p>Aabore et dolore magna aliqua. Quis ipsum suspendisse ultrices gravida. Risus commodo viverra maecenas accumsan lacus vel facilisis.</p>
  </div>
  <a class="btn" style="left:655px;top:398px;width:181px;height:46px;font-weight:600;font-size:14px">GET STARTED›</a>
</section>
<div class="abs stem"></div>
<div class="abs stem-dot"></div>

<section class="careers">
  <p class="abs center eyebrow" style="top:2166px;font-size:13.5px">FEATURED JOBS</p>
  <h2 class="abs center section-title" style="top:2191px"><span class="red">ADVANCED</span> CAREERS</h2>
  <p class="abs center" style="top:2245px;font-size:16.5px;color:var(--ink)">Lorem ipsum dolor sit amet consectetur adipiscing elit, sed do eius</p>
  <div class="abs careers-panel"></div>
  <article class="job" style="left:140px">
    <span class="job-tag">HEALTHCARE</span>
    <h3 class="job-title">Job Offer Heading</h3>
    <p class="job-text">Lorem ipsum dolor sit amet, consectetur adipiscing elit, sed do eiusmod tempo</p>
    <a class="btn job-btn">APPLY NOW ›</a>
  </article>
  <article class="job" style="left:460px">
    <span class="job-tag">IT SERVICES</span>
    <h3 class="job-title">Job Offer Heading</h3>
    <p class="job-text">Lorem ipsum dolor sit amet, consectetur adipiscing elit, sed do eiusmod tempo</p>
    <a class="btn job-btn">APPLY NOW ›</a>
  </article>
  <article class="job" style="left:781px">
    <span class="job-tag">CONSTRUCTION</span>
    <h3 class="job-title">Job Offer Heading</h3>
    <p class="job-text">Lorem ipsum dolor sit amet, consectetur adipiscing elit, sed do eiusmod tempo</p>
    <a class="btn job-btn">APPLY NOW ›</a>
  </article>
  <span class="dot-nav on" style="left:527px"></span>
  <span class="dot-nav" style="left:580px"></span>
  <span class="dot-nav" style="left:634px"></span>
</section>

<section class="testi">
  <p class="abs eyebrow" style="left:134px;top:71px;font-size:15px">TESTIMONIALS</p>
  <h2 class="abs section-title" style="left:134px;top:91px"><span class="red">WHAT PEOPLE</span> ARE SAYING</h2>
  <blockquote class="quote" style="left:136px">
    <span class="quote-mark">“</span>
    <p class="quote-text">Lorem ipsum dolor sit amet, consectetur adipiscing elit, sed do eiusmod tempor incididunt ut labore et dolore magna aliqua Quis ipsum suspendisse ultrices gravida Risus commodo viverra maecenas accumsan lacus vel facilisis.</p>
    <p class="quote-name">Daniel Brooks</p>
    <p class="quote-stars">★★★★★</p>
  </blockquote>
  <blockquote class="quote" style="left:620px">
    <span class="quote-mark">“</span>
    <p class="quote-text">Lorem ipsum dolor sit amet, consectetur adipiscing elit, sed do eiusmod tempor incididunt ut labore et dolore magna aliqua Quis ipsum suspendisse ultrices gravida Risus commodo viverra maecenas accumsan lacus vel facilisis.</p>
    <p class="quote-name">Daniel Brooks</p>
    <p class="quote-stars">★★★★★</p>
  </blockquote>
</section>

<section class="blogs">
  <p class="abs center eyebrow" style="top:3337px;font-size:14px">RESOURCES</p>
  <h2 class="abs center section-title" style="top:3362px"><span class="red">LATEST</span> BLOGS</h2>
  <article class="abs blog-big" role="img" aria-label="Photo of coworkers collaborating around a laptop">
    <span class="date">APR 22, 2025</span>
    <h3>Blog Heading goes here</h3>
    <p>Lorem ipsum dolor sit amet, consectetumet consectetur adipiscing elit, sed do eiusmod tempo</p>
  </article>
  <article class="blog-small" style="top:3447px">
    <div class="photo" role="img" aria-label="Photo of two professionals reviewing a tablet" style="background:linear-gradient(135deg,#5a4a3c,#c7b49a 60%,#8d7a66)"></div>
    <span class="date">APR 22, 2025</span>
    <h3>Blog Heading here</h3>
    <p>Lorem ipsum dolor sit amet, consectetumet consect</p>
  </article>
  <article class="blog-small" style="top:3641px">
    <div class="photo" role="img" aria-label="Photo of a warehouse worker in a safety vest with a clipboard" style="background:linear-gradient(135deg,#6b4a2c,#b89a52 55%,#4a3a2a)"></div>
    <span class="date">APR 22, 2025</span>
    <h3>Blog Heading here</h3>
    <p>Lorem ipsum dolor sit amet, consectetumet consect</p>
  </article>
</section>

<footer class="footer">
  <div class="footer-mark" aria-hidden="true">HALVARD</div>
  <div class="logo" style="left:140px;top:178px">
    <span class="logo-name" style="font-size:38px">HALVARD</span>
    <span class="logo-sub" style="font-size:8.5px">PARTNERING FOR YOUR BUSINESS SUCCESS</span>
  </div>
  <span class="social" style="left:150px"><i></i>Mingleo</span>
  <span class="social" style="left:232px"><i></i>Quillo</span>
  <span class="social" style="left:302px"><i></i>Profilary</span>
  <div class="foot-col" style="left:451px">
    <h4>NAVIGATION</h4>
    <ul><li>Home</li><li>Govertment contracting</li><li>Jobs</li><li>Services</li><li>Contact us</li></ul>
  </div>
  <div class="foot-col" style="left:677px">
    <h4>SERVICES</h4>
    <ul><li>Staffing &amp; Workforce Solutions</li><li>IT Services</li><li>Logistics &amp; Maintenance</li><li>Government Contracting</li></ul>
  </div>
  <div class="foot-col" style="left:941px;top:180px">
    <h4>RESOURCES</h4>
    <ul><li>Blogs</li><li>Testimonials</li><li>Terms of Use</li><li>Privacy Policy</li><li>Sitemap</li></ul>
  </div>
  <p class="copy">Copyright © 2025 Halvard. All Right Reserved</p>
</footer>

<section class="abs cta">
  <div class="cta-glow"></div>
  <p class="eyebrow">GET STARTED</p>
  <h2>DISCOVER OUR SERVICES</h2>
  <p>Lorem ipsum dolor sit amet, consectetur adipiscing elit sed do eiusmod tempor incididunt ut labore et dolore.</p>
  <a class="btn cta-btn">GET STARTED ›</a>
</section>

</body>
</html>
```